Saucy Velvet Impz Business Card

We need business cards designed for our consultants to use and hand out to customers.
We are an Adult party plan company (like Crelvaware but sex toys and lingerie)
We would like bright colours pinks, purples.
The cards need our logo
Space for the reps phone number email address and name.
We need our website on it www.saucyvelvetimps.com.au

```html
<!DOCTYPE html>
<html lang="en">
<head>
<meta charset="utf-8">
<title>Saucy Velvet Impz – Business Card</title>
<link href="https://fonts.googleapis.com/css2?family=Arvo:wght@700&family=Arimo:wght@400&family=Reenie+Beanie&display=swap" rel="stylesheet">
<style>
  :root {
    --backdrop: #e8e5e0;
    --card: #252525;
    --pink: #f0a3cc;
    --pink-fade: rgba(240,163,204,0.28);
    --white: #ffffff;
  }
  * { box-sizing: border-box; margin: 0; padding: 0; }
  html, body {
    width: 1200px;
    height: 1000px;
    overflow: hidden;
    background: var(--backdrop);
  }
  .sheet {
    position: relative;
    width: 1200px;
    height: 1000px;
  }
  .card {
    position: absolute;
    top: 280px;
    width: 440px;
    height: 440px;
    background: var(--card);
    box-shadow: 0 6px 18px rgba(0,0,0,0.18);
  }
  .card--front { left: 110px; }
  .card--back { left: 650px; }

  /* Front: brand lock-up */
  .brand {
    position: absolute;
    left: 0;
    right: 0;
    top: 100px;
    display: flex;
    flex-direction: column;
    align-items: center;
    gap: 26px;
  }
  .brand__mark {
    width: 130px;
    height: 130px;
    background: var(--pink);
  }
  .brand__name {
    font-family: "Arvo", Georgia, serif;
    font-weight: 700;
    font-size: 30px;
    line-height: 1.2;
    color: var(--pink);
    letter-spacing: 0.5px;
    white-space: nowrap;
  }

  /* Back */
  .tail-art {
    position: absolute;
    left: 150px;
    top: 22px;
    width: 250px;
    height: 130px;
    border-radius: 0 0 70px 70px;
    background: linear-gradient(160deg, var(--pink-fade), rgba(240,163,204,0));
  }
  .rep-name {
    position: absolute;
    right: 40px;
    top: 170px;
    font-family: "Reenie Beanie", cursive;
    font-size: 64px;
    line-height: 1;
    color: var(--pink);
    white-space: nowrap;
  }
  .contact {
    position: absolute;
    right: 40px;
    font-family: "Arimo", Arial, sans-serif;
    font-size: 21px;
    color: var(--white);
    text-align: right;
    line-height: 1.3;
    white-space: nowrap;
  }
  .contact--top { top: 258px; }
  .contact--bottom { top: 345px; }
</style>
</head>
<body>
  <main class="sheet">
    <section class="card card--front" aria-label="Business card front">
      <div class="brand">
        <div class="brand__mark" role="img" aria-label="Company logo mark"></div>
        <span class="brand__name">Saucy Velvet Impz</span>
      </div>
    </section>

    <section class="card card--back" aria-label="Business card back">
      <div class="tail-art" role="img" aria-label="Curling pink devil tail ending in a heart"></div>
      <p class="rep-name">Marla Quinn</p>
      <div class="contact contact--top">
        <p class="contact__phone">0400 555 218</p>
        <p class="contact__web">saucyvelvetimps.com.au</p>
      </div>
      <div class="contact contact--bottom">
        <p class="contact__email">marla@saucyvelvetimps.com.au</p>
        <p class="contact__web">www.saucyvelvetimps.com.au</p>
      </div>
    </section>
  </main>
</body>
</html>
```